Bakersfield's Lively Chase 2015 POSTER

Looking for a hip design to attract young 20-30 somethings to a downtown scavenger hunt as a benefit for a local non-profit. Please see our website at www.livelychase.org. Race Date is March 14, 2015, in Downtown Bakersfield.

Industry/Entity Type

Non Profit

```html
<!DOCTYPE html>
<html lang="en">
<head>
<meta charset="utf-8">
<title>Lively Chase 2015 Poster</title>
<link rel="stylesheet" href="https://fonts.googleapis.com/css2?family=Titan+One&family=Londrina+Solid:wght@400;900&display=swap">
<style>
  :root {
    --page: #ffffff;
    --poster-blue: #2a52a0;
    --title-top: #ffe11c;
    --title-bottom: #f04e23;
    --title-edge: #e0251b;
    --white: #ffffff;
    --orange: #f15a24;
  }
  html, body {
    margin: 0;
    padding: 0;
    width: 1200px;
    height: 1000px;
    overflow: hidden;
    background: var(--page);
  }
  .canvas {
    display: block;
    width: 1200px;
    height: 1000px;
  }
  .title {
    font-family: "Titan One", sans-serif;
    font-size: 104px;
  }
  .title-halo { fill: none; stroke: var(--white); stroke-width: 8; stroke-linejoin: round; }
  .title-fill { fill: url(#titleGradient); stroke: var(--title-edge); stroke-width: 1.5; }
  .title-year { fill: var(--white); }
  .tagline {
    font-family: "Londrina Solid", sans-serif;
    font-weight: 900;
    font-size: 78px;
    fill: var(--white);
    stroke: var(--poster-blue);
    stroke-width: 10;
    stroke-linejoin: round;
    paint-order: stroke fill;
  }
  .location {
    font-family: "Londrina Solid", sans-serif;
    font-weight: 400;
    font-size: 72px;
    fill: var(--orange);
  }
</style>
</head>
<body>
<svg class="canvas" viewBox="0 0 1200 1000" xmlns="http://www.w3.org/2000/svg">
  <defs>
    <linearGradient id="titleGradient" x1="0" y1="0" x2="0" y2="1">
      <stop offset="0" stop-color="var(--title-top)"/>
      <stop offset="1" stop-color="var(--title-bottom)"/>
    </linearGradient>
    <linearGradient id="tileStreet" x1="0" y1="0" x2="0" y2="1"><stop offset="0" stop-color="#c9a98a"/><stop offset="1" stop-color="#b83a3a"/></linearGradient>
    <linearGradient id="tileTwins" x1="0" y1="0" x2="0" y2="1"><stop offset="0" stop-color="#d8b48a"/><stop offset="1" stop-color="#b7e04a"/></linearGradient>
    <linearGradient id="tileRunner" x1="0" y1="0" x2="0" y2="1"><stop offset="0" stop-color="#6f8a4a"/><stop offset="1" stop-color="#c4c4c4"/></linearGradient>
    <linearGradient id="tileMasks" x1="0" y1="0" x2="0" y2="1"><stop offset="0" stop-color="#d9b07e"/><stop offset="1" stop-color="#6a3c8c"/></linearGradient>
    <linearGradient id="tileBalloons" x1="0" y1="0" x2="0" y2="1"><stop offset="0" stop-color="#f1d6d6"/><stop offset="1" stop-color="#3a6fc4"/></linearGradient>
    <linearGradient id="tileThings" x1="0" y1="0" x2="0" y2="1"><stop offset="0" stop-color="#d7ae80"/><stop offset="1" stop-color="#c8262e"/></linearGradient>
    <linearGradient id="tileBlueWigs" x1="0" y1="0" x2="0" y2="1"><stop offset="0" stop-color="#6b8fa8"/><stop offset="1" stop-color="#1f5bc0"/></linearGradient>
    <linearGradient id="tileCheck" x1="0" y1="0" x2="0" y2="1"><stop offset="0" stop-color="#e4e2dc"/><stop offset="1" stop-color="#c34b47"/></linearGradient>
    <linearGradient id="tileMedals" x1="0" y1="0" x2="0" y2="1"><stop offset="0" stop-color="#b7323e"/><stop offset="1" stop-color="#b89a5a"/></linearGradient>
  </defs>

  <g class="poster">
    <rect class="poster-board" x="310" y="70" width="580" height="860" fill="var(--poster-blue)"/>

    <g class="poster-title">
      <text class="title title-halo" x="600" y="188" text-anchor="middle" textLength="540" lengthAdjust="spacingAndGlyphs">LIVELY</text>
      <text class="title title-fill" x="600" y="188" text-anchor="middle" textLength="540" lengthAdjust="spacingAndGlyphs">LIVELY</text>
      <text class="title title-halo" x="330" y="285" textLength="290" lengthAdjust="spacingAndGlyphs">CHASE</text>
      <text class="title title-fill" x="330" y="285" textLength="290" lengthAdjust="spacingAndGlyphs">CHASE</text>
      <text class="title title-year" x="640" y="285" textLength="232" lengthAdjust="spacingAndGlyphs">2015</text>
    </g>

    <g class="photo-grid">
      <g role="img" aria-label="Photo: finish line on a downtown street with balloon arch and red carpet"><rect x="350" y="326" width="149" height="149" fill="url(#tileStreet)"/></g>
      <g role="img" aria-label="Photo: two racers in matching neon twin shirts"><rect x="526" y="326" width="149" height="149" fill="url(#tileTwins)"/></g>
      <g role="img" aria-label="Photo: racer with bib number in the street"><rect x="701" y="326" width="149" height="149" fill="url(#tileRunner)"/></g>
      <g role="img" aria-label="Photo: team in purple outfits and masquerade masks"><rect x="350" y="497" width="149" height="149" fill="url(#tileMasks)"/></g>
      <g role="img" aria-label="Photo: racers under balloons at the start"><rect x="526" y="497" width="149" height="149" fill="url(#tileBalloons)"/></g>
      <g role="img" aria-label="Photo: team in red shirts and blue wigs"><rect x="701" y="497" width="149" height="149" fill="url(#tileThings)"/></g>
      <g role="img" aria-label="Photo: racer in blue wig and mask holding a medal"><rect x="350" y="667" width="149" height="149" fill="url(#tileBlueWigs)"/></g>
      <g role="img" aria-label="Photo: winning team receiving a check"><rect x="526" y="667" width="149" height="149" fill="url(#tileCheck)"/></g>
      <g role="img" aria-label="Photo: finisher medals with red and blue ribbons"><rect x="701" y="667" width="149" height="149" fill="url(#tileMedals)"/></g>
    </g>

    <text class="tagline" x="0" y="0" text-anchor="middle" textLength="740" lengthAdjust="spacingAndGlyphs" transform="translate(610 600) rotate(-41)">TEST YOUR CITY LIMITS!</text>

    <text class="location" x="600" y="902" text-anchor="middle" textLength="558" lengthAdjust="spacingAndGlyphs">DOWNTOWN BAKERSFIELD</text>
  </g>
</svg>
</body>
</html>
```